We are a building company that build new homes and units we are looking for something fresh and looks good my company name is
Orland Building Group Pty Ltd

Industry/Entity Type

Building

Contact Information for Business Card

Name Marco Deluca-Finn
Tittle: Director
Address 14 Larkmoor St. Pellingwood Vic 3091
Ph: 03 9512 4386
Mobile : 0400 736 294

www.orlandbuildinggroup.com.au
Email: sales@orlandbuildinggroup.com.au

```html
<!DOCTYPE html>
<html lang="en">
<head>
<meta charset="utf-8">
<title>Orland Building Group – Business Card</title>
<link rel="stylesheet" href="https://fonts.googleapis.com/css2?family=Michroma&family=Saira+Condensed:wght@400&family=Kalam:wght@400&display=swap">
<style>
  :root {
    --sky: #18b7ee;
    --sky-light: #3fc6f3;
    --slate: #55575a;
    --slate-deep: #393a3d;
    --slate-edge: #2e2f31;
    --white: #ffffff;
    --page: #ffffff;
  }
  * { margin: 0; padding: 0; box-sizing: border-box; }
  html, body {
    width: 993px;
    height: 1200px;
    overflow: hidden;
    background: var(--page);
  }
  .card {
    position: absolute;
    left: 55px;
    width: 881px;
    overflow: hidden;
    color: var(--white);
  }
  .card--front { top: 45px; height: 545px; }
  .card--back  { top: 610px; height: 548px; }
  .card__bg {
    position: absolute;
    inset: 0;
    width: 100%;
    height: 100%;
  }
  .wordmark {
    position: absolute;
    font-family: "Michroma", sans-serif;
    font-weight: 400;
    color: var(--white);
    line-height: 1.3;
    letter-spacing: 0.12em;
    text-transform: uppercase;
  }
  .card--front .wordmark { left: 397px; top: 300px; font-size: 25px; }
  .card--back .wordmark  { left: 88px;  top: 68px;  font-size: 25px; }
  .rule-front {
    position: absolute;
    left: 333px; right: 0; top: 400px;
    height: 2px;
    background: var(--white);
  }
  .tagline {
    position: absolute;
    font-family: "Kalam", cursive;
    color: var(--white);
    white-space: nowrap;
  }
  .card--front .tagline { left: 403px; top: 418px; font-size: 24px; }
  .card--back .tagline  { left: 92px;  top: 160px; font-size: 24px; }
  .accent-bar {
    position: absolute;
    left: 53px; top: 62px;
    width: 2px; height: 134px;
    background: var(--white);
  }
  .contact {
    position: absolute;
    right: 90px;
    top: 270px;
    text-align: right;
    font-family: "Saira Condensed", sans-serif;
    color: var(--white);
  }
  .contact__name {
    font-size: 36px;
    letter-spacing: 0.03em;
    line-height: 44px;
    text-transform: uppercase;
  }
  .contact__rule {
    width: 392px;
    height: 2px;
    margin: 0 -4px 6px auto;
    background: linear-gradient(to right, rgba(255,255,255,0), var(--white) 40%);
  }
  .contact__line { font-size: 31px; line-height: 41px; }
  .contact__line--web { font-size: 29px; line-height: 39px; }
</style>
</head>
<body>

<section class="card card--front" aria-label="Business card front">
  <svg class="card__bg" viewBox="0 0 750 464" preserveAspectRatio="none" aria-hidden="true">
    <defs>
      <linearGradient id="skyFront" x1="0" y1="0" x2="0" y2="1">
        <stop offset="0" stop-color="#3fc6f3"/>
        <stop offset="1" stop-color="#0fb0ea"/>
      </linearGradient>
      <linearGradient id="slateFront" x1="0" y1="0" x2="0" y2="1">
        <stop offset="0" stop-color="#5c5e61"/>
        <stop offset="1" stop-color="#38393c"/>
      </linearGradient>
    </defs>
    <rect width="750" height="464" fill="url(#skyFront)"/>
    <path d="M0,262 C260,250 540,180 728,0 L750,0 L750,464 L0,464 Z" fill="#2e2f31"/>
    <path d="M0,274 C260,262 560,196 750,22 L750,464 L0,464 Z" fill="url(#slateFront)"/>
  </svg>
  <div class="wordmark">Orland Building<br>Group</div>
  <div class="rule-front"></div>
  <p class="tagline">Quality, excellence and innovation</p>
</section>

<section class="card card--back" aria-label="Business card back">
  <svg class="card__bg" viewBox="0 0 750 466" preserveAspectRatio="none" aria-hidden="true">
    <defs>
      <linearGradient id="skyBack" x1="0" y1="0" x2="0" y2="1">
        <stop offset="0" stop-color="#3fc6f3"/>
        <stop offset="1" stop-color="#0fb0ea"/>
      </linearGradient>
      <linearGradient id="slateBack" x1="0" y1="0" x2="0" y2="1">
        <stop offset="0" stop-color="#5c5e61"/>
        <stop offset="1" stop-color="#38393c"/>
      </linearGradient>
    </defs>
    <rect width="750" height="466" fill="url(#skyBack)"/>
    <path d="M0,256 C280,250 560,170 738,0 L750,0 L750,466 L0,466 Z" fill="#2e2f31"/>
    <path d="M0,268 C290,262 580,186 750,14 L750,466 L0,466 Z" fill="url(#slateBack)"/>
  </svg>
  <div class="accent-bar"></div>
  <div class="wordmark">Orland Building<br>Group</div>
  <p class="tagline">New home design and construction</p>
  <div class="contact">
    <p class="contact__name">Marco Deluca-Finn</p>
    <div class="contact__rule"></div>
    <p class="contact__line">Ph: 03 9512 4386</p>
    <p class="contact__line">Mobile: 0400 736 294</p>
    <p class="contact__line contact__line--web">www.orlandbuildinggroup.com.au</p>
    <p class="contact__line contact__line--web">Email: sales@orlandbuildinggroup.com.au</p>
  </div>
</section>

</body>
</html>
```